Digital Transformation Company Template Slidedeck

I am looking for help designing a set of standard business powerpoint slides that are branded specifically for my company. I have attached more details and the logo design file that can be used for this project. Thanks!

Target Market(s)

Small and Medium Businesses

```html
<!DOCTYPE html>
<html lang="en">
<head>
<meta charset="utf-8">
<title>Nexora Digital — Slide Deck Overview</title>
<link href="https://fonts.googleapis.com/css2?family=Montserrat:wght@400;500;600;700;800&display=swap" rel="stylesheet">
<style>
:root{
  --navy:#1f3b5e;
  --navy-deep:#16283f;
  --navy-mid:#27476e;
  --orange:#f0892a;
  --blue:#3a8fd3;
  --teal:#2fb3a6;
  --red:#e2574c;
  --green:#7cb342;
  --muted:#6f7b89;
  --muted-dark:#a9b7c7;
  --line:#d8dee6;
  --line-dark:#3d5878;
  --paper:#ffffff;
  --canvas:#e9edf2;
  --photo-a:#6f7e8e;
  --photo-b:#c4ae95;
}
*{box-sizing:border-box;margin:0;padding:0}
html,body{width:885px;height:1200px;overflow:hidden;background:var(--canvas);font-family:"Montserrat",Arial,sans-serif}
.deck{display:grid;grid-template-columns:repeat(5,171px);grid-auto-rows:96px;gap:4px 6px;padding:2px 3px;width:885px;height:1200px}
.slide{position:relative;overflow:hidden;background:var(--paper);color:var(--navy);box-shadow:0 0 0 1px #d9dee5}
.slide.dark{background:var(--navy-deep);color:#fff;box-shadow:none}
.abs{position:absolute}
.hd{position:absolute;left:9px;top:7px;font-weight:700;font-size:6.5px;border-left:2px solid var(--orange);padding-left:3px;line-height:7px;white-space:nowrap}
.sub{position:absolute;left:14px;top:15px;font-size:3.8px;color:var(--muted);white-space:nowrap}
.dark .sub{color:var(--muted-dark)}
.p{position:absolute;font-size:3.8px;line-height:5.2px;color:var(--muted)}
.dark .p{color:var(--muted-dark)}
.h5{position:absolute;font-size:4.6px;font-weight:700;line-height:5.5px;white-space:nowrap}
.c{text-align:center}
.w{color:#fff}
.ph{position:absolute;background:linear-gradient(135deg,var(--photo-a),var(--photo-b))}
.dark .ph{background:linear-gradient(135deg,#4c6079,#a08c76)}
.card{position:absolute;background:var(--navy);border-radius:2px}
.dark .card{background:var(--navy-mid)}
.box{position:absolute;border:1px solid var(--line);border-radius:2px;background:#f5f7fa}
.dark .box{background:var(--navy-mid);border-color:var(--line-dark)}
.dot{position:absolute;border-radius:50%}
.o{background:var(--orange)}.n{background:var(--navy)}.b{background:var(--blue)}.t{background:var(--teal)}.r{background:var(--red)}.g{background:var(--green)}
.dark .n{background:#5d7ea6}
.ic{position:absolute;fill:none;stroke:currentColor;stroke-width:2.6;stroke-linecap:round;stroke-linejoin:round;color:#fff}
.ic.fo{color:var(--orange)}
.bars{position:absolute;display:flex;align-items:flex-end;justify-content:space-around;border-bottom:1px solid var(--line)}
.dark .bars{border-color:var(--line-dark)}
.bars i{display:block;width:6px}
.axis{position:absolute;display:flex;justify-content:space-around;font-size:3.4px;color:var(--muted)}
.dark .axis{color:var(--muted-dark)}
.big{position:absolute;font-weight:800;font-size:10.5px;line-height:11.5px}
.brand{position:absolute;font-weight:700;font-size:5.5px;color:var(--orange);display:flex;align-items:center;gap:2px}
.brand .mark{width:4px;height:4px;background:var(--orange)}
.num{position:absolute;font-weight:800;font-size:8px;line-height:9px;color:var(--orange)}
table.tb{position:absolute;border-collapse:collapse;font-size:3.6px}
.tb th{background:var(--navy);color:#fff;padding:1.6px 3px;font-weight:600;text-align:left}
.dark .tb th{background:var(--orange)}
.tb td{padding:1.6px 3px;border-bottom:1px solid var(--line);color:var(--muted)}
.dark .tb td{border-color:var(--line-dark);color:var(--muted-dark)}
.tb td:first-child{font-weight:600;color:var(--navy)}
.dark .tb td:first-child{color:#fff}
.pin{position:absolute;width:1px;background:var(--line)}
.dark .pin{background:var(--line-dark)}
.rule{position:absolute;height:1px;background:var(--line)}
.dark .rule{background:var(--line-dark)}
.mapfill{position:absolute;background:linear-gradient(180deg,#cbd5df,#aebccb);border-radius:3px}
.dark .mapfill{background:linear-gradient(180deg,#3a5578,#2a4262)}
.btn{position:absolute;background:var(--orange);color:#fff;font-size:3.8px;font-weight:700;padding:1.6px 4px;border-radius:1px}
.tag{position:absolute;font-size:3.4px;font-weight:600;color:var(--muted)}
.dark .tag{color:var(--muted-dark)}
.legend{position:absolute;font-size:3.6px;color:var(--muted);line-height:6px}
.dark .legend{color:var(--muted-dark)}
.legend b{display:inline-block;width:4px;height:4px;margin-right:2px;vertical-align:-0.5px}
</style>
</head>
<body>
<svg width="0" height="0" style="position:absolute" aria-hidden="true">
  <symbol id="i-check" viewBox="0 0 24 24"><polyline points="5,12 10,17 19,7"/></symbol>
  <symbol id="i-arrow" viewBox="0 0 24 24"><line x1="5" y1="12" x2="19" y2="12"/><polyline points="13,6 19,12 13,18"/></symbol>
  <symbol id="i-pin" viewBox="0 0 24 24"><path d="M12 22s-7-7-7-12a7 7 0 0 1 14 0c0 5-7 12-7 12z"/><circle cx="12" cy="10" r="2.5"/></symbol>
  <symbol id="i-phone" viewBox="0 0 24 24"><rect x="7" y="2" width="10" height="20" rx="2"/><line x1="11" y1="18" x2="13" y2="18"/></symbol>
  <symbol id="i-gear" viewBox="0 0 24 24"><circle cx="12" cy="12" r="3.5"/><path d="M12 3v3M12 18v3M3 12h3M18 12h3M5.6 5.6l2.1 2.1M16.3 16.3l2.1 2.1M5.6 18.4l2.1-2.1M16.3 7.7l2.1-2.1"/></symbol>
  <symbol id="i-bars" viewBox="0 0 24 24"><line x1="6" y1="20" x2="6" y2="13"/><line x1="12" y1="20" x2="12" y2="8"/><line x1="18" y1="20" x2="18" y2="4"/></symbol>
  <symbol id="i-cloud" viewBox="0 0 24 24"><path d="M7 18h10a4 4 0 0 0 0-8 6 6 0 0 0-11.5 1.5A3.3 3.3 0 0 0 7 18z"/></symbol>
  <symbol id="i-shield" viewBox="0 0 24 24"><path d="M12 3l8 3v6c0 5-4 8-8 9-4-1-8-4-8-9V6z"/></symbol>
  <symbol id="i-star" viewBox="0 0 24 24"><polygon points="12,3 14.8,9 21,9.5 16.3,13.8 17.8,20 12,16.6 6.2,20 7.7,13.8 3,9.5 9.2,9"/></symbol>
  <symbol id="i-mail" viewBox="0 0 24 24"><rect x="3" y="5" width="18" height="14" rx="1"/><polyline points="3,6 12,13 21,6"/></symbol>
  <symbol id="i-bulb" viewBox="0 0 24 24"><circle cx="12" cy="10" r="6"/><line x1="9" y1="20" x2="15" y2="20"/></symbol>
  <symbol id="i-target" viewBox="0 0 24 24"><circle cx="12" cy="12" r="8"/><circle cx="12" cy="12" r="4"/><circle cx="12" cy="12" r="0.8"/></symbol>
</svg>

<main class="deck">

<!-- ================= LIGHT THEME ================= -->
<section class="slide">
  <div class="ph" style="left:70px;top:0;width:101px;height:96px;clip-path:polygon(25% 0,100% 0,100% 100%,0 100%)" role="img" aria-label="Team working in a modern office"></div>
  <div class="abs o" style="left:62px;top:0;width:14px;height:96px;clip-path:polygon(60% 0,100% 0,40% 100%,0 100%)"></div>
  <p class="brand" style="left:9px;top:9px"><span class="mark"></span>Nexora</p>
  <h2 class="big" style="left:9px;top:34px">Business<br>Presentation</h2>
  <p class="p" style="left:9px;top:59px">Digital transformation</p>
  <p class="tag" style="left:9px;top:80px">Company Profile 2024</p>
</section>
<section class="slide">
  <div class="ph" style="left:8px;top:10px;width:36px;height:36px" role="img" aria-label="Laptop on a desk"></div>
  <div class="ph" style="left:47px;top:10px;width:36px;height:36px" role="img" aria-label="Meeting room"></div>
  <div class="ph" style="left:8px;top:49px;width:75px;height:36px" role="img" aria-label="Team discussion"></div>
  <h2 class="big" style="left:92px;top:24px">Business<br>Proposal</h2>
  <div class="abs o" style="left:92px;top:50px;width:20px;height:2px"></div>
  <p class="p" style="left:92px;top:56px;width:72px">Strategy, design and cloud services that help small teams grow faster.</p>
</section>
<section class="slide">
  <h3 class="hd">Pricing Table</h3><p class="sub">Choose the plan that fits your team</p>
  <table class="tb" style="left:9px;top:24px;width:153px">
    <tr><th>Plan</th><th>Basic</th><th>Pro</th><th>Team</th></tr>
    <tr><td>Users</td><td>5</td><td>20</td><td>50</td></tr>
    <tr><td>Storage</td><td>10GB</td><td>50GB</td><td>1TB</td></tr>
    <tr><td>Support</td><td>Email</td><td>Chat</td><td>24/7</td></tr>
    <tr><td>Price</td><td>$19</td><td>$49</td><td>$99</td></tr>
  </table>
  <div class="btn" style="left:120px;top:80px">Get Started</div>
</section>
<section class="slide">
  <h3 class="hd">Our Team</h3><p class="sub">People behind every project</p>
  <div class="ph" style="left:10px;top:24px;width:33px;height:38px" role="img" aria-label="Team member portrait"></div>
  <div class="ph" style="left:49px;top:24px;width:33px;height:38px" role="img" aria-label="Team member portrait"></div>
  <div class="ph" style="left:88px;top:24px;width:33px;height:38px" role="img" aria-label="Team member portrait"></div>
  <div class="ph" style="left:127px;top:24px;width:33px;height:38px" role="img" aria-label="Team member portrait"></div>
  <p class="h5 c" style="left:10px;top:66px;width:33px">CEO</p><p class="h5 c" style="left:49px;top:66px;width:33px">CTO</p><p class="h5 c" style="left:88px;top:66px;width:33px">Design</p><p class="h5 c" style="left:127px;top:66px;width:33px">Sales</p>
  <p class="p c" style="left:10px;top:73px;width:33px">Founder</p><p class="p c" style="left:49px;top:73px;width:33px">Engineering</p><p class="p c" style="left:88px;top:73px;width:33px">Creative</p><p class="p c" style="left:127px;top:73px;width:33px">Growth</p>
</section>
<section class="slide">
  <h3 class="hd">About Us</h3>
  <p class="p" style="left:9px;top:20px;width:74px">We guide small and medium businesses through digital change with clear plans and simple tools.</p>
  <p class="num" style="left:9px;top:56px">12+</p><p class="tag" style="left:9px;top:66px">Years</p>
  <p class="num" style="left:40px;top:56px">250</p><p class="tag" style="left:40px;top:66px">Clients</p>
  <div class="ph" style="left:88px;top:0;width:83px;height:96px;clip-path:polygon(20% 0,100% 0,100% 100%,0 100%)" role="img" aria-label="Business team photo"></div>
</section>

<section class="slide">
  <div class="ph" style="left:0;top:0;width:70px;height:96px" role="img" aria-label="Person working at a desk"></div>
  <h3 class="hd" style="left:78px;top:14px">Our Mission</h3>
  <p class="p" style="left:78px;top:26px;width:84px">Make modern technology simple, affordable and useful for every growing business.</p>
  <div class="btn" style="left:78px;top:60px">Learn More</div>
</section>
<section class="slide">
  <h3 class="hd">Our Services</h3>
  <div class="card" style="left:9px;top:20px;width:48px;height:66px"></div>
  <div class="card" style="left:62px;top:20px;width:48px;height:66px"></div>
  <div class="card" style="left:115px;top:20px;width:48px;height:66px"></div>
  <div class="dot o" style="left:27px;top:26px;width:12px;height:12px"></div><svg class="ic" style="left:30px;top:29px" width="6" height="6"><use href="#i-cloud"/></svg>
  <div class="dot o" style="left:80px;top:26px;width:12px;height:12px"></div><svg class="ic" style="left:83px;top:29px" width="6" height="6"><use href="#i-bars"/></svg>
  <div class="dot o" style="left:133px;top:26px;width:12px;height:12px"></div><svg class="ic" style="left:136px;top:29px" width="6" height="6"><use href="#i-shield"/></svg>
  <p class="h5 c w" style="left:9px;top:44px;width:48px">Cloud</p><p class="h5 c w" style="left:62px;top:44px;width:48px">Data</p><p class="h5 c w" style="left:115px;top:44px;width:48px">Security</p>
  <p class="p c" style="left:12px;top:53px;width:42px;color:#b9c6d6">Move your work to fast, safe servers.</p>
  <p class="p c" style="left:65px;top:53px;width:42px;color:#b9c6d6">Turn numbers into clear decisions.</p>
  <p class="p c" style="left:118px;top:53px;width:42px;color:#b9c6d6">Protect files, users and devices.</p>
</section>
<section class="slide">
  <h3 class="hd">Our Values</h3><p class="sub">What drives our daily work</p>
  <div class="dot b" style="left:16px;top:27px;width:22px;height:22px"></div><svg class="ic" style="left:21.5px;top:32.5px" width="11" height="11"><use href="#i-bulb"/></svg>
  <div class="dot n" style="left:54px;top:27px;width:22px;height:22px"></div><svg class="ic" style="left:59.5px;top:32.5px" width="11" height="11"><use href="#i-shield"/></svg>
  <div class="dot o" style="left:92px;top:27px;width:22px;height:22px"></div><svg class="ic" style="left:97.5px;top:32.5px" width="11" height="11"><use href="#i-star"/></svg>
  <div class="dot t" style="left:130px;top:27px;width:22px;height:22px"></div><svg class="ic" style="left:135.5px;top:32.5px" width="11" height="11"><use href="#i-target"/></svg>
  <p class="h5 c" style="left:9px;top:54px;width:36px">Ideas</p><p class="h5 c" style="left:47px;top:54px;width:36px">Trust</p><p class="h5 c" style="left:85px;top:54px;width:36px">Quality</p><p class="h5 c" style="left:123px;top:54px;width:36px">Focus</p>
  <p class="p c" style="left:9px;top:62px;width:36px">Fresh thinking</p><p class="p c" style="left:47px;top:62px;width:36px">Open and honest</p><p class="p c" style="left:85px;top:62px;width:36px">Work done right</p><p class="p c" style="left:123px;top:62px;width:36px">Clear results</p>
</section>
<section class="slide">
  <h3 class="hd">Portfolio</h3><p class="sub">Recent client projects</p>
  <div class="ph" style="left:9px;top:23px;width:48px;height:30px" role="img" aria-label="Project image"></div>
  <div class="ph" style="left:61px;top:23px;width:48px;height:30px" role="img" aria-label="Project image"></div>
  <div class="ph" style="left:113px;top:23px;width:49px;height:30px" role="img" aria-label="Project image"></div>
  <div class="ph" style="left:9px;top:57px;width:48px;height:30px" role="img" aria-label="Project image"></div>
  <div class="ph" style="left:61px;top:57px;width:48px;height:30px" role="img" aria-label="Project image"></div>
  <div class="ph" style="left:113px;top:57px;width:49px;height:30px" role="img" aria-label="Project image"></div>
</section>
<section class="slide">
  <h3 class="hd">Timeline</h3><p class="sub">How we have grown</p>
  <div class="rule" style="left:10px;top:44px;width:150px"></div>
  <div class="dot b" style="left:13px;top:37px;width:14px;height:14px"></div><svg class="ic" style="left:16.5px;top:40.5px" width="7" height="7"><use href="#i-star"/></svg>
  <div class="dot n" style="left:51px;top:37px;width:14px;height:14px"></div><svg class="ic" style="left:54.5px;top:40.5px" width="7" height="7"><use href="#i-gear"/></svg>
  <div class="dot o" style="left:89px;top:37px;width:14px;height:14px"></div><svg class="ic" style="left:92.5px;top:40.5px" width="7" height="7"><use href="#i-cloud"/></svg>
  <div class="dot t" style="left:127px;top:37px;width:14px;height:14px"></div><svg class="ic" style="left:130.5px;top:40.5px" width="7" height="7"><use href="#i-target"/></svg>
  <p class="h5 c" style="left:5px;top:56px;width:30px">2021</p><p class="h5 c" style="left:43px;top:56px;width:30px">2022</p><p class="h5 c" style="left:81px;top:56px;width:30px">2023</p><p class="h5 c" style="left:119px;top:56px;width:30px">2024</p>
  <p class="p c" style="left:5px;top:63px;width:30px">Founded</p><p class="p c" style="left:43px;top:63px;width:30px">New team</p><p class="p c" style="left:81px;top:63px;width:30px">Cloud launch</p><p class="p c" style="left:119px;top:63px;width:30px">250 clients</p>
</section>

<section class="slide">
  <h3 class="hd">Features</h3><p class="sub">Everything in one platform</p>
  <div class="dot b" style="left:14px;top:26px;width:18px;height:18px"></div><svg class="ic" style="left:18.5px;top:30.5px" width="9" height="9"><use href="#i-cloud"/></svg>
  <div class="dot o" style="left:45px;top:26px;width:18px;height:18px"></div><svg class="ic" style="left:49.5px;top:30.5px" width="9" height="9"><use href="#i-bars"/></svg>
  <div class="dot r" style="left:76px;top:26px;width:18px;height:18px"></div><svg class="ic" style="left:80.5px;top:30.5px" width="9" height="9"><use href="#i-shield"/></svg>
  <div class="dot t" style="left:107px;top:26px;width:18px;height:18px"></div><svg class="ic" style="left:111.5px;top:30.5px" width="9" height="9"><use href="#i-gear"/></svg>
  <div class="dot g" style="left:138px;top:26px;width:18px;height:18px"></div><svg class="ic" style="left:142.5px;top:30.5px" width="9" height="9"><use href="#i-phone"/></svg>
  <p class="h5 c" style="left:8px;top:50px;width:30px">Storage</p><p class="h5 c" style="left:39px;top:50px;width:30px">Reports</p><p class="h5 c" style="left:70px;top:50px;width:30px">Safety</p><p class="h5 c" style="left:101px;top:50px;width:30px">Automate</p><p class="h5 c" style="left:132px;top:50px;width:30px">Mobile</p>
  <p class="p c" style="left:8px;top:58px;width:30px">Files anywhere</p><p class="p c" style="left:39px;top:58px;width:30px">Live insight</p><p class="p c" style="left:70px;top:58px;width:30px">Data protection</p><p class="p c" style="left:101px;top:58px;width:30px">Fewer tasks</p><p class="p c" style="left:132px;top:58px;width:30px">Work on the go</p>
</section>
<section class="slide dark">
  <h3 class="hd">Comparison</h3>
  <table class="tb" style="left:9px;top:20px;width:153px">
    <tr><th>Feature</th><th>Nexora</th><th>Others</th></tr>
    <tr><td>Setup time</td><td>1 day</td><td>2 weeks</td></tr>
    <tr><td>Support</td><td>24/7</td><td>Office hours</td></tr>
    <tr><td>Cloud backup</td><td>Included</td><td>Extra</td></tr>
    <tr><td>Training</td><td>Free</td><td>Paid</td></tr>
    <tr><td>Monthly cost</td><td>$49</td><td>$89</td></tr>
  </table>
</section>
<section class="slide">
  <h3 class="hd">Strategy</h3>
  <div class="box" style="left:9px;top:20px;width:74px;height:32px"></div>
  <div class="box" style="left:88px;top:20px;width:74px;height:32px"></div>
  <div class="box" style="left:9px;top:56px;width:74px;height:32px"></div>
  <div class="box" style="left:88px;top:56px;width:74px;height:32px"></div>
  <div class="dot o" style="left:13px;top:25px;width:10px;height:10px"></div><svg class="ic" style="left:15.5px;top:27.5px" width="5" height="5"><use href="#i-target"/></svg>
  <div class="dot b" style="left:92px;top:25px;width:10px;height:10px"></div><svg class="ic" style="left:94.5px;top:27.5px" width="5" height="5"><use href="#i-bulb"/></svg>
  <div class="dot t" style="left:13px;top:61px;width:10px;height:10px"></div><svg class="ic" style="left:15.5px;top:63.5px" width="5" height="5"><use href="#i-gear"/></svg>
  <div class="dot n" style="left:92px;top:61px;width:10px;height:10px"></div><svg class="ic" style="left:94.5px;top:63.5px" width="5" height="5"><use href="#i-bars"/></svg>
  <p class="h5" style="left:26px;top:27px">Analyse</p><p class="h5" style="left:105px;top:27px">Plan</p><p class="h5" style="left:26px;top:63px">Build</p><p class="h5" style="left:105px;top:63px">Measure</p>
  <p class="p" style="left:13px;top:38px;width:66px">Review current tools and goals.</p>
  <p class="p" style="left:92px;top:38px;width:66px">Set a clear path and budget.</p>
  <p class="p" style="left:13px;top:74px;width:66px">Roll out new systems in steps.</p>
  <p class="p" style="left:92px;top:74px;width:66px">Track results and improve.</p>
</section>
<section class="slide">
  <div class="ph" style="left:0;top:0;width:62px;height:96px" role="img" aria-label="Developer working at a computer"></div>
  <h3 class="hd" style="left:70px">Workflow</h3>
  <div class="card" style="left:70px;top:22px;width:43px;height:30px;background:var(--orange)"></div>
  <div class="card" style="left:118px;top:22px;width:44px;height:30px"></div>
  <p class="h5 w" style="left:74px;top:26px;font-size:7px;line-height:8px">01</p><p class="h5 w" style="left:122px;top:26px;font-size:7px;line-height:8px">02</p>
  <p class="h5 w" style="left:74px;top:36px">Discover</p><p class="h5 w" style="left:122px;top:36px">Deliver</p>
  <p class="p w" style="left:74px;top:43px">Listen first</p><p class="p" style="left:122px;top:43px;color:#b9c6d6">Ship on time</p>
  <p class="p" style="left:70px;top:58px;width:92px">A simple two step method keeps every project clear, fast and on budget.</p>
</section>
<section class="slide">
  <h3 class="hd">Statistics</h3><p class="sub">Yearly performance</p>
  <div class="bars" style="left:12px;top:24px;width:112px;height:56px">
    <i class="n" style="height:30%"></i><i class="o" style="height:45%"></i><i class="n" style="height:55%"></i><i class="o" style="height:40%"></i><i class="n" style="height:70%"></i><i class="o" style="height:60%"></i><i class="n" style="height:85%"></i><i class="o" style="height:75%"></i><i class="n" style="height:95%"></i>
  </div>
  <div class="axis" style="left:12px;top:82px;width:112px"><span>Q1</span><span>Q2</span><span>Q3</span><span>Q4</span></div>
  <div class="legend" style="left:130px;top:28px"><b class="n"></b>Sales<br><b class="o"></b>Profit</div>
  <p class="num" style="left:130px;top:46px">+38%</p><p class="p" style="left:130px;top:56px;width:34px">Growth this year</p>
</section>

<section class="slide">
  <h3 class="hd">Case Study</h3>
  <div class="ph" style="left:9px;top:20px;width:70px;height:66px" role="img" aria-label="Client at work"></div>
  <p class="h5" style="left:86px;top:21px">Retail Client</p>
  <p class="p" style="left:86px;top:28px;width:76px">Moved sales, stock and reports to one cloud system in eight weeks.</p>
  <p class="num" style="left:86px;top:58px">+45%</p><p class="p" style="left:86px;top:68px">Faster orders</p>
  <p class="num" style="left:124px;top:58px">-30%</p><p class="p" style="left:124px;top:68px">Lower costs</p>
</section>
<section class="slide">
  <h3 class="hd">Benefits</h3>
  <div class="card" style="left:9px;top:20px;width:36px;height:34px;background:var(--orange)"></div><svg class="ic" style="left:21px;top:31px" width="12" height="12"><use href="#i-check"/></svg>
  <div class="card" style="left:49px;top:20px;width:36px;height:34px"></div><svg class="ic" style="left:61px;top:31px" width="12" height="12"><use href="#i-bars"/></svg>
  <div class="card" style="left:89px;top:20px;width:36px;height:34px;background:var(--orange)"></div><svg class="ic" style="left:101px;top:31px" width="12" height="12"><use href="#i-shield"/></svg>
  <div class="card" style="left:129px;top:20px;width:34px;height:34px"></div><svg class="ic" style="left:140px;top:31px" width="12" height="12"><use href="#i-star"/></svg>
  <p class="h5 c" style="left:9px;top:59px;width:36px">Simple</p><p class="h5 c" style="left:49px;top:59px;width:36px">Scalable</p><p class="h5 c" style="left:89px;top:59px;width:36px">Secure</p><p class="h5 c" style="left:129px;top:59px;width:34px">Trusted</p>
  <p class="p c" style="left:9px;top:67px;width:36px">Easy to use</p><p class="p c" style="left:49px;top:67px;width:36px">Grows with you</p><p class="p c" style="left:89px;top:67px;width:36px">Safe by design</p><p class="p c" style="left:129px;top:67px;width:34px">250 clients</p>
</section>
<section class="slide">
  <div class="abs" style="left:0;top:0;width:171px;height:96px;background:var(--navy);clip-path:polygon(0 0,60% 0,40% 100%,0 100%)"></div>
  <div class="ph" style="left:80px;top:14px;width:80px;height:66px" role="img" aria-label="Growth concept photo"></div>
  <h2 class="big w" style="left:10px;top:30px">Growth<br>Plan</h2>
  <div class="abs o" style="left:10px;top:57px;width:22px;height:2px"></div>
  <p class="p" style="left:10px;top:62px;width:52px;color:#b9c6d6">Three year path to scale</p>
</section>
<section class="slide">
  <h3 class="hd">Process</h3>
  <div class="pin" style="left:26px;top:44px;height:30px"></div><div class="dot b" style="left:17px;top:24px;width:20px;height:20px"></div><svg class="ic" style="left:22px;top:29px" width="10" height="10"><use href="#i-bulb"/></svg>
  <div class="pin" style="left:63px;top:44px;height:30px"></div><div class="dot o" style="left:54px;top:24px;width:20px;height:20px"></div><svg class="ic" style="left:59px;top:29px" width="10" height="10"><use href="#i-target"/></svg>
  <div class="pin" style="left:100px;top:44px;height:30px"></div><div class="dot t" style="left:91px;top:24px;width:20px;height:20px"></div><svg class="ic" style="left:96px;top:29px" width="10" height="10"><use href="#i-gear"/></svg>
  <div class="pin" style="left:137px;top:44px;height:30px"></div><div class="dot r" style="left:128px;top:24px;width:20px;height:20px"></div><svg class="ic" style="left:133px;top:29px" width="10" height="10"><use href="#i-check"/></svg>
  <p class="h5" style="left:29px;top:50px">01</p><p class="h5" style="left:66px;top:50px">02</p><p class="h5" style="left:103px;top:50px">03</p><p class="h5" style="left:140px;top:50px">04</p>
  <p class="p" style="left:29px;top:57px">Idea</p><p class="p" style="left:66px;top:57px">Goal</p><p class="p" style="left:103px;top:57px">Build</p><p class="p" style="left:140px;top:57px">Done</p>
  <div class="rule" style="left:10px;top:78px;width:150px"></div>
</section>
<section class="slide">
  <h3 class="hd">Revenue</h3><p class="sub">Monthly income in $k</p>
  <div class="bars" style="left:12px;top:24px;width:148px;height:56px">
    <i class="n" style="height:35%;width:9px"></i><i class="n" style="height:50%;width:9px"></i><i class="o" style="height:62%;width:9px"></i><i class="n" style="height:45%;width:9px"></i><i class="n" style="height:70%;width:9px"></i><i class="o" style="height:85%;width:9px"></i><i class="n" style="height:60%;width:9px"></i><i class="n" style="height:95%;width:9px"></i>
  </div>
  <div class="axis" style="left:12px;top:82px;width:148px"><span>Jan</span><span>Feb</span><span>Mar</span><span>Apr</span><span>May</span><span>Jun</span><span>Jul</span><span>Aug</span></div>
</section>

<section class="slide">
  <div class="ph" style="left:0;top:0;width:80px;height:96px" role="img" aria-label="Professional portrait"></div>
  <h3 class="hd" style="left:88px;top:14px">Our Goals</h3>
  <svg class="ic fo" style="left:88px;top:28px" width="5" height="5"><use href="#i-check"/></svg><p class="p" style="left:95px;top:28px">Serve 500 clients</p>
  <svg class="ic fo" style="left:88px;top:37px" width="5" height="5"><use href="#i-check"/></svg><p class="p" style="left:95px;top:37px">Open two offices</p>
  <svg class="ic fo" style="left:88px;top:46px" width="5" height="5"><use href="#i-check"/></svg><p class="p" style="left:95px;top:46px">Launch mobile app</p>
  <svg class="ic fo" style="left:88px;top:55px" width="5" height="5"><use href="#i-check"/></svg><p class="p" style="left:95px;top:55px">Double revenue</p>
  <div class="dot o" style="left:88px;top:70px;width:7px;height:7px"></div><div class="dot n" style="left:99px;top:70px;width:7px;height:7px"></div>
</section>
<section class="slide">
  <h3 class="hd">Market Share</h3><p class="sub">Share by service line</p>
  <div class="bars" style="left:12px;top:26px;width:94px;height:58px">
    <i class="n" style="height:85%;width:10px"></i><i class="o" style="height:60%;width:10px"></i><i class="n" style="height:45%;width:10px"></i><i class="o" style="height:30%;width:10px"></i>
  </div>
  <div class="legend" style="left:114px;top:28px"><b class="n"></b>Cloud 42%<br><b class="o"></b>Data 28%<br><b class="n"></b>Apps 18%<br><b class="o"></b>Other 12%</div>
</section>
<section class="slide">
  <h3 class="hd">Milestones</h3><p class="sub">Key wins so far</p>
  <div class="dot o" style="left:14px;top:26px;width:18px;height:18px"></div><svg class="ic" style="left:18.5px;top:30.5px" width="9" height="9"><use href="#i-star"/></svg>
  <div class="dot b" style="left:55px;top:26px;width:18px;height:18px"></div><svg class="ic" style="left:59.5px;top:30.5px" width="9" height="9"><use href="#i-target"/></svg>
  <div class="dot r" style="left:96px;top:26px;width:18px;height:18px"></div><svg class="ic" style="left:100.5px;top:30.5px" width="9" height="9"><use href="#i-bars"/></svg>
  <div class="dot g" style="left:137px;top:26px;width:18px;height:18px"></div><svg class="ic" style="left:141.5px;top:30.5px" width="9" height="9"><use href="#i-check"/></svg>
  <p class="h5 c" style="left:5px;top:50px;width:36px">100</p><p class="h5 c" style="left:46px;top:50px;width:36px">15</p><p class="h5 c" style="left:87px;top:50px;width:36px">$2M</p><p class="h5 c" style="left:128px;top:50px;width:36px">98%</p>
  <p class="p c" style="left:5px;top:57px;width:36px">Projects</p><p class="p c" style="left:46px;top:57px;width:36px">Awards</p><p class="p c" style="left:87px;top:57px;width:36px">Revenue</p><p class="p c" style="left:128px;top:57px;width:36px">Happy clients</p>
</section>
<section class="slide">
  <h3 class="hd">Roadmap</h3>
  <div class="abs" style="left:10px;top:50px;width:150px;height:2px;background:var(--navy)"></div>
  <div class="dot o" style="left:18px;top:46px;width:10px;height:10px"></div>
  <div class="dot o" style="left:56px;top:46px;width:10px;height:10px"></div>
  <div class="dot o" style="left:94px;top:46px;width:10px;height:10px"></div>
  <div class="dot o" style="left:132px;top:46px;width:10px;height:10px"></div>
  <p class="h5" style="left:14px;top:27px">Plan</p><p class="p" style="left:14px;top:34px">Month 1</p>
  <p class="h5" style="left:52px;top:60px">Build</p><p class="p" style="left:52px;top:67px">Month 2–3</p>
  <p class="h5" style="left:90px;top:27px">Test</p><p class="p" style="left:90px;top:34px">Month 4</p>
  <p class="h5" style="left:126px;top:60px">Launch</p><p class="p" style="left:126px;top:67px">Month 5</p>
</section>
<section class="slide">
  <h3 class="hd">Solutions</h3>
  <div class="card" style="left:9px;top:20px;width:49px;height:32px;background:var(--green)"></div>
  <div class="card" style="left:61px;top:20px;width:49px;height:32px;background:var(--orange)"></div>
  <div class="card" style="left:113px;top:20px;width:49px;height:32px;background:var(--red)"></div>
  <div class="card" style="left:9px;top:56px;width:49px;height:32px;background:var(--blue)"></div>
  <div class="card" style="left:61px;top:56px;width:49px;height:32px;background:var(--teal)"></div>
  <div class="card" style="left:113px;top:56px;width:49px;height:32px"></div>
  <svg class="ic" style="left:29px;top:25px" width="9" height="9"><use href="#i-cloud"/></svg><p class="h5 c w" style="left:9px;top:39px;width:49px">Cloud</p>
  <svg class="ic" style="left:81px;top:25px" width="9" height="9"><use href="#i-bars"/></svg><p class="h5 c w" style="left:61px;top:39px;width:49px">Analytics</p>
  <svg class="ic" style="left:133px;top:25px" width="9" height="9"><use href="#i-shield"/></svg><p class="h5 c w" style="left:113px;top:39px;width:49px">Security</p>
  <svg class="ic" style="left:29px;top:61px" width="9" height="9"><use href="#i-phone"/></svg><p class="h5 c w" style="left:9px;top:75px;width:49px">Mobile</p>
  <svg class="ic" style="left:81px;top:61px" width="9" height="9"><use href="#i-gear"/></svg><p class="h5 c w" style="left:61px;top:75px;width:49px">Automation</p>
  <svg class="ic" style="left:133px;top:61px" width="9" height="9"><use href="#i-mail"/></svg><p class="h5 c w" style="left:113px;top:75px;width:49px">Support</p>
</section>

<section class="slide">
  <h3 class="hd">Dashboard</h3>
  <div class="box" style="left:9px;top:20px;width:82px;height:58px;background:#eef2f6"></div>
  <div class="abs" style="left:9px;top:78px;width:82px;height:4px;background:var(--line);border-radius:0 0 3px 3px"></div>
  <svg class="abs" style="left:14px;top:30px" width="72" height="42" viewBox="0 0 72 42"><polyline points="0,36 12,27 24,30 36,17 48,21 60,9 72,4" fill="none" stroke="#f0892a" stroke-width="2"/></svg>
  <p class="num" style="left:98px;top:22px">1,240</p><p class="p" style="left:98px;top:32px">Active users</p>
  <p class="num" style="left:98px;top:44px">86%</p><p class="p" style="left:98px;top:54px">Uptime score</p>
  <p class="p" style="left:98px;top:66px;width:64px">Live view of your key numbers.</p>
</section>
<section class="slide">
  <h3 class="hd">Introduction</h3>
  <p class="p" style="left:9px;top:20px;width:72px">Nexora helps small and medium businesses adopt the right digital tools. We plan, build and support systems that save time.</p>
  <p class="p" style="left:90px;top:20px;width:72px">Our team blends strategy, design and engineering so every client gets clear advice and lasting results.</p>
  <div class="btn" style="left:9px;top:76px">Read More</div>
</section>
<section class="slide">
  <h3 class="hd">Global Reach</h3><p class="sub">Clients in 18 countries</p>
  <div class="mapfill" style="left:12px;top:24px;width:110px;height:62px" role="img" aria-label="World map"></div>
  <svg class="ic fo" style="left:38px;top:36px" width="7" height="7"><use href="#i-pin"/></svg><svg class="ic fo" style="left:74px;top:33px" width="7" height="7"><use href="#i-pin"/></svg><svg class="ic fo" style="left:100px;top:58px" width="7" height="7"><use href="#i-pin"/></svg>
  <p class="num" style="left:128px;top:28px">18</p><p class="p" style="left:128px;top:38px">Countries</p>
  <p class="num" style="left:128px;top:52px">3</p><p class="p" style="left:128px;top:62px">Regions</p>
</section>
<section class="slide">
  <h3 class="hd">Locations</h3>
  <div class="mapfill" style="left:10px;top:20px;width:100px;height:66px" role="img" aria-label="United States map"></div>
  <svg class="ic fo" style="left:30px;top:38px" width="7" height="7"><use href="#i-pin"/></svg><svg class="ic fo" style="left:86px;top:46px" width="7" height="7"><use href="#i-pin"/></svg>
  <p class="h5" style="left:116px;top:26px">West Office</p><p class="p" style="left:116px;top:33px">Sales and support</p>
  <p class="h5" style="left:116px;top:46px">East Office</p><p class="p" style="left:116px;top:53px">Engineering</p>
</section>
<section class="slide">
  <div class="ph" style="left:0;top:0;width:171px;height:96px;background:linear-gradient(135deg,#8e959c,#5f6770)" role="img" aria-label="Office background in grey"></div>
  <h2 class="big w" style="left:12px;top:30px">Thank You</h2>
  <svg class="ic" style="left:12px;top:50px" width="5" height="5"><use href="#i-phone"/></svg><p class="p w" style="left:19px;top:50px">+1 000 555 0199</p>
  <svg class="ic" style="left:12px;top:59px" width="5" height="5"><use href="#i-mail"/></svg><p class="p w" style="left:19px;top:59px">hello@nexora.co</p>
</section>

<!-- ================= DARK THEME ================= -->
<section class="slide dark">
  <div class="ph" style="left:70px;top:0;width:101px;height:96px;clip-path:polygon(25% 0,100% 0,100% 100%,0 100%)" role="img" aria-label="Team working in a modern office"></div>
  <div class="abs o" style="left:62px;top:0;width:14px;height:96px;clip-path:polygon(60% 0,100% 0,40% 100%,0 100%)"></div>
  <p class="brand" style="left:9px;top:9px"><span class="mark"></span>Nexora</p>
  <h2 class="big" style="left:9px;top:34px">Business<br>Presentation</h2>
  <p class="p" style="left:9px;top:59px">Digital transformation</p>
  <p class="tag" style="left:9px;top:80px">Company Profile 2024</p>
</section>
<section class="slide dark">
  <div class="ph" style="left:8px;top:10px;width:36px;height:36px" role="img" aria-label="Laptop on a desk"></div>
  <div class="ph" style="left:47px;top:10px;width:36px;height:36px" role="img" aria-label="Meeting room"></div>
  <div class="ph" style="left:8px;top:49px;width:75px;height:36px" role="img" aria-label="Team discussion"></div>
  <h2 class="big" style="left:92px;top:24px">Business<br>Proposal</h2>
  <div class="abs o" style="left:92px;top:50px;width:20px;height:2px"></div>
  <p class="p" style="left:92px;top:56px;width:72px">Strategy, design and cloud services that help small teams grow faster.</p>
</section>
<section class="slide dark">
  <h3 class="hd">Pricing Table</h3><p class="sub">Choose the plan that fits your team</p>
  <table class="tb" style="left:9px;top:24px;width:153px">
    <tr><th>Plan</th><th>Basic</th><th>Pro</th><th>Team</th></tr>
    <tr><td>Users</td><td>5</td><td>20</td><td>50</td></tr>
    <tr><td>Storage</td><td>10GB</td><td>50GB</td><td>1TB</td></tr>
    <tr><td>Support</td><td>Email</td><td>Chat</td><td>24/7</td></tr>
    <tr><td>Price</td><td>$19</td><td>$49</td><td>$99</td></tr>
  </table>
  <div class="btn" style="left:120px;top:80px">Get Started</div>
</section>
<section class="slide dark">
  <h3 class="hd">Our Team</h3><p class="sub">People behind every project</p>
  <div class="ph" style="left:10px;top:24px;width:33px;height:38px" role="img" aria-label="Team member portrait"></div>
  <div class="ph" style="left:49px;top:24px;width:33px;height:38px" role="img" aria-label="Team member portrait"></div>
  <div class="ph" style="left:88px;top:24px;width:33px;height:38px" role="img" aria-label="Team member portrait"></div>
  <div class="ph" style="left:127px;top:24px;width:33px;height:38px" role="img" aria-label="Team member portrait"></div>
  <p class="h5 c" style="left:10px;top:66px;width:33px">CEO</p><p class="h5 c" style="left:49px;top:66px;width:33px">CTO</p><p class="h5 c" style="left:88px;top:66px;width:33px">Design</p><p class="h5 c" style="left:127px;top:66px;width:33px">Sales</p>
  <p class="p c" style="left:10px;top:73px;width:33px">Founder</p><p class="p c" style="left:49px;top:73px;width:33px">Engineering</p><p class="p c" style="left:88px;top:73px;width:33px">Creative</p><p class="p c" style="left:127px;top:73px;width:33px">Growth</p>
</section>
<section class="slide dark">
  <h3 class="hd">About Us</h3>
  <p class="p" style="left:9px;top:20px;width:74px">We guide small and medium businesses through digital change with clear plans and simple tools.</p>
  <p class="num" style="left:9px;top:56px">12+</p><p class="tag" style="left:9px;top:66px">Years</p>
  <p class="num" style="left:40px;top:56px">250</p><p class="tag" style="left:40px;top:66px">Clients</p>
  <div class="ph" style="left:88px;top:0;width:83px;height:96px;clip-path:polygon(20% 0,100% 0,100% 100%,0 100%)" role="img" aria-label="Business team photo"></div>
</section>

<section class="slide dark">
  <div class="ph" style="left:0;top:0;width:70px;height:96px" role="img" aria-label="Person working at a desk"></div>
  <h3 class="hd" style="left:78px;top:14px">Our Mission</h3>
  <p class="p" style="left:78px;top:26px;width:84px">Make modern technology simple, affordable and useful for every growing business.</p>
  <div class="btn" style="left:78px;top:60px">Learn More</div>
</section>
<section class="slide dark">
  <h3 class="hd">Our Services</h3>
  <div class="card" style="left:9px;top:20px;width:48px;height:66px"></div>
  <div class="card" style="left:62px;top:20px;width:48px;height:66px"></div>
  <div class="card" style="left:115px;top:20px;width:48px;height:66px"></div>
  <div class="dot o" style="left:27px;top:26px;width:12px;height:12px"></div><svg class="ic" style="left:30px;top:29px" width="6" height="6"><use href="#i-cloud"/></svg>
  <div class="dot o" style="left:80px;top:26px;width:12px;height:12px"></div><svg class="ic" style="left:83px;top:29px" width="6" height="6"><use href="#i-bars"/></svg>
  <div class="dot o" style="left:133px;top:26px;width:12px;height:12px"></div><svg class="ic" style="left:136px;top:29px" width="6" height="6"><use href="#i-shield"/></svg>
  <p class="h5 c" style="left:9px;top:44px;width:48px">Cloud</p><p class="h5 c" style="left:62px;top:44px;width:48px">Data</p><p class="h5 c" style="left:115px;top:44px;width:48px">Security</p>
  <p class="p c" style="left:12px;top:53px;width:42px">Move your work to fast, safe servers.</p>
  <p class="p c" style="left:65px;top:53px;width:42px">Turn numbers into clear decisions.</p>
  <p class="p c" style="left:118px;top:53px;width:42px">Protect files, users and devices.</p>
</section>
<section class="slide dark">
  <h3 class="hd">Our Values</h3><p class="sub">What drives our daily work</p>
  <div class="dot b" style="left:16px;top:27px;width:22px;height:22px"></div><svg class="ic" style="left:21.5px;top:32.5px" width="11" height="11"><use href="#i-bulb"/></svg>
  <div class="dot n" style="left:54px;top:27px;width:22px;height:22px"></div><svg class="ic" style="left:59.5px;top:32.5px" width="11" height="11"><use href="#i-shield"/></svg>
  <div class="dot o" style="left:92px;top:27px;width:22px;height:22px"></div><svg class="ic" style="left:97.5px;top:32.5px" width="11" height="11"><use href="#i-star"/></svg>
  <div class="dot t" style="left:130px;top:27px;width:22px;height:22px"></div><svg class="ic" style="left:135.5px;top:32.5px" width="11" height="11"><use href="#i-target"/></svg>
  <p class="h5 c" style="left:9px;top:54px;width:36px">Ideas</p><p class="h5 c" style="left:47px;top:54px;width:36px">Trust</p><p class="h5 c" style="left:85px;top:54px;width:36px">Quality</p><p class="h5 c" style="left:123px;top:54px;width:36px">Focus</p>
  <p class="p c" style="left:9px;top:62px;width:36px">Fresh thinking</p><p class="p c" style="left:47px;top:62px;width:36px">Open and honest</p><p class="p c" style="left:85px;top:62px;width:36px">Work done right</p><p class="p c" style="left:123px;top:62px;width:36px">Clear results</p>
</section>
<section class="slide dark">
  <h3 class="hd">Portfolio</h3><p class="sub">Recent client projects</p>
  <div class="ph" style="left:9px;top:23px;width:48px;height:30px" role="img" aria-label="Project image"></div>
  <div class="ph" style="left:61px;top:23px;width:48px;height:30px" role="img" aria-label="Project image"></div>
  <div class="ph" style="left:113px;top:23px;width:49px;height:30px" role="img" aria-label="Project image"></div>
  <div class="ph" style="left:9px;top:57px;width:48px;height:30px" role="img" aria-label="Project image"></div>
  <div class="ph" style="left:61px;top:57px;width:48px;height:30px" role="img" aria-label="Project image"></div>
  <div class="ph" style="left:113px;top:57px;width:49px;height:30px" role="img" aria-label="Project image"></div>
</section>
<section class="slide dark">
  <h3 class="hd">Timeline</h3><p class="sub">How we have grown</p>
  <div class="rule" style="left:10px;top:44px;width:150px"></div>
  <div class="dot b" style="left:13px;top:37px;width:14px;height:14px"></div><svg class="ic" style="left:16.5px;top:40.5px" width="7" height="7"><use href="#i-star"/></svg>
  <div class="dot n" style="left:51px;top:37px;width:14px;height:14px"></div><svg class="ic" style="left:54.5px;top:40.5px" width="7" height="7"><use href="#i-gear"/></svg>
  <div class="dot o" style="left:89px;top:37px;width:14px;height:14px"></div><svg class="ic" style="left:92.5px;top:40.5px" width="7" height="7"><use href="#i-cloud"/></svg>
  <div class="dot t" style="left:127px;top:37px;width:14px;height:14px"></div><svg class="ic" style="left:130.5px;top:40.5px" width="7" height="7"><use href="#i-target"/></svg>
  <p class="h5 c" style="left:5px;top:56px;width:30px">2021</p><p class="h5 c" style="left:43px;top:56px;width:30px">2022</p><p class="h5 c" style="left:81px;top:56px;width:30px">2023</p><p class="h5 c" style="left:119px;top:56px;width:30px">2024</p>
  <p class="p c" style="left:5px;top:63px;width:30px">Founded</p><p class="p c" style="left:43px;top:63px;width:30px">New team</p><p class="p c" style="left:81px;top:63px;width:30px">Cloud launch</p><p class="p c" style="left:119px;top:63px;width:30px">250 clients</p>
</section>

<section class="slide dark">
  <h3 class="hd">Features</h3><p class="sub">Everything in one platform</p>
  <div class="dot b" style="left:14px;top:26px;width:18px;height:18px"></div><svg class="ic" style="left:18.5px;top:30.5px" width="9" height="9"><use href="#i-cloud"/></svg>
  <div class="dot o" style="left:45px;top:26px;width:18px;height:18px"></div><svg class="ic" style="left:49.5px;top:30.5px" width="9" height="9"><use href="#i-bars"/></svg>
  <div class="dot r" style="left:76px;top:26px;width:18px;height:18px"></div><svg class="ic" style="left:80.5px;top:30.5px" width="9" height="9"><use href="#i-shield"/></svg>
  <div class="dot t" style="left:107px;top:26px;width:18px;height:18px"></div><svg class="ic" style="left:111.5px;top:30.5px" width="9" height="9"><use href="#i-gear"/></svg>
  <div class="dot g" style="left:138px;top:26px;width:18px;height:18px"></div><svg class="ic" style="left:142.5px;top:30.5px" width="9" height="9"><use href="#i-phone"/></svg>
  <p class="h5 c" style="left:8px;top:50px;width:30px">Storage</p><p class="h5 c" style="left:39px;top:50px;width:30px">Reports</p><p class="h5 c" style="left:70px;top:50px;width:30px">Safety</p><p class="h5 c" style="left:101px;top:50px;width:30px">Automate</p><p class="h5 c" style="left:132px;top:50px;width:30px">Mobile</p>
  <p class="p c" style="left:8px;top:58px;width:30px">Files anywhere</p><p class="p c" style="left:39px;top:58px;width:30px">Live insight</p><p class="p c" style="left:70px;top:58px;width:30px">Data protection</p><p class="p c" style="left:101px;top:58px;width:30px">Fewer tasks</p><p class="p c" style="left:132px;top:58px;width:30px">Work on the go</p>
</section>
<section class="slide dark">
  <h3 class="hd">Comparison</h3>
  <table class="tb" style="left:9px;top:20px;width:153px">
    <tr><th>Feature</th><th>Nexora</th><th>Others</th></tr>
    <tr><td>Setup time</td><td>1 day</td><td>2 weeks</td></tr>
    <tr><td>Support</td><td>24/7</td><td>Office hours</td></tr>
    <tr><td>Cloud backup</td><td>Included</td><td>Extra</td></tr>
    <tr><td>Training</td><td>Free</td><td>Paid</td></tr>
    <tr><td>Monthly cost</td><td>$49</td><td>$89</td></tr>
  </table>
</section>
<section class="slide dark">
  <h3 class="hd">Strategy</h3>
  <div class="box" style="left:9px;top:20px;width:74px;height:32px"></div>
  <div class="box" style="left:88px;top:20px;width:74px;height:32px"></div>
  <div class="box" style="left:9px;top:56px;width:74px;height:32px"></div>
  <div class="box" style="left:88px;top:56px;width:74px;height:32px"></div>
  <div class="dot o" style="left:13px;top:25px;width:10px;height:10px"></div><svg class="ic" style="left:15.5px;top:27.5px" width="5" height="5"><use href="#i-target"/></svg>
  <div class="dot b" style="left:92px;top:25px;width:10px;height:10px"></div><svg class="ic" style="left:94.5px;top:27.5px" width="5" height="5"><use href="#i-bulb"/></svg>
  <div class="dot t" style="left:13px;top:61px;width:10px;height:10px"></div><svg class="ic" style="left:15.5px;top:63.5px" width="5" height="5"><use href="#i-gear"/></svg>
  <div class="dot o" style="left:92px;top:61px;width:10px;height:10px"></div><svg class="ic" style="left:94.5px;top:63.5px" width="5" height="5"><use href="#i-bars"/></svg>
  <p class="h5" style="left:26px;top:27px">Analyse</p><p class="h5" style="left:105px;top:27px">Plan</p><p class="h5" style="left:26px;top:63px">Build</p><p class="h5" style="left:105px;top:63px">Measure</p>
  <p class="p" style="left:13px;top:38px;width:66px">Review current tools and goals.</p>
  <p class="p" style="left:92px;top:38px;width:66px">Set a clear path and budget.</p>
  <p class="p" style="left:13px;top:74px;width:66px">Roll out new systems in steps.</p>
  <p class="p" style="left:92px;top:74px;width:66px">Track results and improve.</p>
</section>
<section class="slide dark">
  <div class="ph" style="left:0;top:0;width:62px;height:96px" role="img" aria-label="Developer working at a computer"></div>
  <h3 class="hd" style="left:70px">Workflow</h3>
  <div class="card" style="left:70px;top:22px;width:43px;height:30px;background:var(--orange)"></div>
  <div class="card" style="left:118px;top:22px;width:44px;height:30px"></div>
  <p class="h5" style="left:74px;top:26px;font-size:7px;line-height:8px">01</p><p class="h5" style="left:122px;top:26px;font-size:7px;line-height:8px">02</p>
  <p class="h5" style="left:74px;top:36px">Discover</p><p class="h5" style="left:122px;top:36px">Deliver</p>
  <p class="p w" style="left:74px;top:43px">Listen first</p><p class="p" style="left:122px;top:43px">Ship on time</p>
  <p class="p" style="left:70px;top:58px;width:92px">A simple two step method keeps every project clear, fast and on budget.</p>
</section>
<section class="slide dark">
  <h3 class="hd">Statistics</h3><p class="sub">Yearly performance</p>
  <div class="bars" style="left:12px;top:24px;width:112px;height:56px">
    <i class="b" style="height:30%"></i><i class="o" style="height:45%"></i><i class="b" style="height:55%"></i><i class="o" style="height:40%"></i><i class="b" style="height:70%"></i><i class="o" style="height:60%"></i><i class="b" style="height:85%"></i><i class="o" style="height:75%"></i><i class="b" style="height:95%"></i>
  </div>
  <div class="axis" style="left:12px;top:82px;width:112px"><span>Q1</span><span>Q2</span><span>Q3</span><span>Q4</span></div>
  <div class="legend" style="left:130px;top:28px"><b class="b"></b>Sales<br><b class="o"></b>Profit</div>
  <p class="num" style="left:130px;top:46px">+38%</p><p class="p" style="left:130px;top:56px;width:34px">Growth this year</p>
</section>

<section class="slide dark">
  <h3 class="hd">Case Study</h3>
  <div class="ph" style="left:9px;top:20px;width:70px;height:66px" role="img" aria-label="Client at work"></div>
  <p class="h5" style="left:86px;top:21px">Retail Client</p>
  <p class="p" style="left:86px;top:28px;width:76px">Moved sales, stock and reports to one cloud system in eight weeks.</p>
  <p class="num" style="left:86px;top:58px">+45%</p><p class="p" style="left:86px;top:68px">Faster orders</p>
  <p class="num" style="left:124px;top:58px">-30%</p><p class="p" style="left:124px;top:68px">Lower costs</p>
</section>
<section class="slide dark">
  <h3 class="hd">Benefits</h3>
  <div class="card" style="left:9px;top:20px;width:36px;height:34px;background:var(--orange)"></div><svg class="ic" style="left:21px;top:31px" width="12" height="12"><use href="#i-check"/></svg>
  <div class="card" style="left:49px;top:20px;width:36px;height:34px"></div><svg class="ic" style="left:61px;top:31px" width="12" height="12"><use href="#i-bars"/></svg>
  <div class="card" style="left:89px;top:20px;width:36px;height:34px;background:var(--orange)"></div><svg class="ic" style="left:101px;top:31px" width="12" height="12"><use href="#i-shield"/></svg>
  <div class="card" style="left:129px;top:20px;width:34px;height:34px"></div><svg class="ic" style="left:140px;top:31px" width="12" height="12"><use href="#i-star"/></svg>
  <p class="h5 c" style="left:9px;top:59px;width:36px">Simple</p><p class="h5 c" style="left:49px;top:59px;width:36px">Scalable</p><p class="h5 c" style="left:89px;top:59px;width:36px">Secure</p><p class="h5 c" style="left:129px;top:59px;width:34px">Trusted</p>
  <p class="p c" style="left:9px;top:67px;width:36px">Easy to use</p><p class="p c" style="left:49px;top:67px;width:36px">Grows with you</p><p class="p c" style="left:89px;top:67px;width:36px">Safe by design</p><p class="p c" style="left:129px;top:67px;width:34px">250 clients</p>
</section>
<section class="slide dark">
  <div class="abs" style="left:0;top:0;width:171px;height:96px;background:var(--orange);clip-path:polygon(0 0,60% 0,40% 100%,0 100%)"></div>
  <div class="ph" style="left:80px;top:14px;width:80px;height:66px" role="img" aria-label="Growth concept photo"></div>
  <h2 class="big" style="left:10px;top:30px">Growth<br>Plan</h2>
  <div class="abs" style="left:10px;top:57px;width:22px;height:2px;background:#fff"></div>
  <p class="p w" style="left:10px;top:62px;width:52px">Three year path to scale</p>
</section>
<section class="slide dark">
  <h3 class="hd">Process</h3>
  <div class="pin" style="left:26px;top:44px;height:30px"></div><div class="dot b" style="left:17px;top:24px;width:20px;height:20px"></div><svg class="ic" style="left:22px;top:29px" width="10" height="10"><use href="#i-bulb"/></svg>
  <div class="pin" style="left:63px;top:44px;height:30px"></div><div class="dot o" style="left:54px;top:24px;width:20px;height:20px"></div><svg class="ic" style="left:59px;top:29px" width="10" height="10"><use href="#i-target"/></svg>
  <div class="pin" style="left:100px;top:44px;height:30px"></div><div class="dot t" style="left:91px;top:24px;width:20px;height:20px"></div><svg class="ic" style="left:96px;top:29px" width="10" height="10"><use href="#i-gear"/></svg>
  <div class="pin" style="left:137px;top:44px;height:30px"></div><div class="dot r" style="left:128px;top:24px;width:20px;height:20px"></div><svg class="ic" style="left:133px;top:29px" width="10" height="10"><use href="#i-check"/></svg>
  <p class="h5" style="left:29px;top:50px">01</p><p class="h5" style="left:66px;top:50px">02</p><p class="h5" style="left:103px;top:50px">03</p><p class="h5" style="left:140px;top:50px">04</p>
  <p class="p" style="left:29px;top:57px">Idea</p><p class="p" style="left:66px;top:57px">Goal</p><p class="p" style="left:103px;top:57px">Build</p><p class="p" style="left:140px;top:57px">Done</p>
  <div class="rule" style="left:10px;top:78px;width:150px"></div>
</section>
<section class="slide dark">
  <h3 class="hd">Revenue</h3><p class="sub">Monthly income in $k</p>
  <div class="bars" style="left:12px;top:24px;width:148px;height:56px">
    <i class="b" style="height:35%;width:9px"></i><i class="b" style="height:50%;width:9px"></i><i class="o" style="height:62%;width:9px"></i><i class="b" style="height:45%;width:9px"></i><i class="b" style="height:70%;width:9px"></i><i class="o" style="height:85%;width:9px"></i><i class="b" style="height:60%;width:9px"></i><i class="b" style="height:95%;width:9px"></i>
  </div>
  <div class="axis" style="left:12px;top:82px;width:148px"><span>Jan</span><span>Feb</span><span>Mar</span><span>Apr</span><span>May</span><span>Jun</span><span>Jul</span><span>Aug</span></div>
</section>

<section class="slide dark">
  <div class="ph" style="left:0;top:0;width:80px;height:96px" role="img" aria-label="Professional portrait"></div>
  <h3 class="hd" style="left:88px;top:14px">Our Goals</h3>
  <svg class="ic fo" style="left:88px;top:28px" width="5" height="5"><use href="#i-check"/></svg><p class="p" style="left:95px;top:28px">Serve 500 clients</p>
  <svg class="ic fo" style="left:88px;top:37px" width="5" height="5"><use href="#i-check"/></svg><p class="p" style="left:95px;top:37px">Open two offices</p>
  <svg class="ic fo" style="left:88px;top:46px" width="5" height="5"><use href="#i-check"/></svg><p class="p" style="left:95px;top:46px">Launch mobile app</p>
  <svg class="ic fo" style="left:88px;top:55px" width="5" height="5"><use href="#i-check"/></svg><p class="p" style="left:95px;top:55px">Double revenue</p>
  <div class="dot o" style="left:88px;top:70px;width:7px;height:7px"></div><div class="dot b" style="left:99px;top:70px;width:7px;height:7px"></div>
</section>
<section class="slide dark">
  <h3 class="hd">Mobile App</h3>
  <div class="box" style="left:20px;top:20px;width:30px;height:68px;border-radius:5px" role="img" aria-label="App screen mockup"></div>
  <div class="box" style="left:58px;top:20px;width:30px;height:68px;border-radius:5px" role="img" aria-label="App screen mockup"></div>
  <p class="h5" style="left:98px;top:24px">Work anywhere</p>
  <p class="p" style="left:98px;top:32px;width:64px">Track tasks, sales and reports from your phone.</p>
  <svg class="ic fo" style="left:98px;top:58px" width="5" height="5"><use href="#i-check"/></svg><p class="p" style="left:105px;top:58px">iOS and Android</p>
  <svg class="ic fo" style="left:98px;top:67px" width="5" height="5"><use href="#i-check"/></svg><p class="p" style="left:105px;top:67px">Offline mode</p>
</section>
<section class="slide dark">
  <h3 class="hd">Milestones</h3><p class="sub">Key wins so far</p>
  <div class="dot o" style="left:14px;top:26px;width:18px;height:18px"></div><svg class="ic" style="left:18.5px;top:30.5px" width="9" height="9"><use href="#i-star"/></svg>
  <div class="dot b" style="left:55px;top:26px;width:18px;height:18px"></div><svg class="ic" style="left:59.5px;top:30.5px" width="9" height="9"><use href="#i-target"/></svg>
  <div class="dot r" style="left:96px;top:26px;width:18px;height:18px"></div><svg class="ic" style="left:100.5px;top:30.5px" width="9" height="9"><use href="#i-bars"/></svg>
  <div class="dot g" style="left:137px;top:26px;width:18px;height:18px"></div><svg class="ic" style="left:141.5px;top:30.5px" width="9" height="9"><use href="#i-check"/></svg>
  <p class="h5 c" style="left:5px;top:50px;width:36px">100</p><p class="h5 c" style="left:46px;top:50px;width:36px">15</p><p class="h5 c" style="left:87px;top:50px;width:36px">$2M</p><p class="h5 c" style="left:128px;top:50px;width:36px">98%</p>
  <p class="p c" style="left:5px;top:57px;width:36px">Projects</p><p class="p c" style="left:46px;top:57px;width:36px">Awards</p><p class="p c" style="left:87px;top:57px;width:36px">Revenue</p><p class="p c" style="left:128px;top:57px;width:36px">Happy clients</p>
</section>
<section class="slide dark">
  <h3 class="hd">Roadmap</h3>
  <div class="abs" style="left:10px;top:50px;width:150px;height:2px;background:var(--blue)"></div>
  <div class="dot o" style="left:18px;top:46px;width:10px;height:10px"></div>
  <div class="dot o" style="left:56px;top:46px;width:10px;height:10px"></div>
  <div class="dot o" style="left:94px;top:46px;width:10px;height:10px"></div>
  <div class="dot o" style="left:132px;top:46px;width:10px;height:10px"></div>
  <p class="h5" style="left:14px;top:27px">Plan</p><p class="p" style="left:14px;top:34px">Month 1</p>
  <p class="h5" style="left:52px;top:60px">Build</p><p class="p" style="left:52px;top:67px">Month 2–3</p>
  <p class="h5" style="left:90px;top:27px">Test</p><p class="p" style="left:90px;top:34px">Month 4</p>
  <p class="h5" style="left:126px;top:60px">Launch</p><p class="p" style="left:126px;top:67px">Month 5</p>
</section>
<section class="slide dark">
  <h3 class="hd">Growth Rate</h3><p class="sub">Client growth by year</p>
  <div class="bars" style="left:12px;top:24px;width:148px;height:56px">
    <i class="b" style="height:25%;width:8px"></i><i class="b" style="height:38%;width:8px"></i><i class="b" style="height:48%;width:8px"></i><i class="o" style="height:60%;width:8px"></i><i class="b" style="height:55%;width:8px"></i><i class="b" style="height:72%;width:8px"></i><i class="o" style="height:88%;width:8px"></i><i class="b" style="height:80%;width:8px"></i><i class="b" style="height:96%;width:8px"></i>
  </div>
  <div class="axis" style="left:12px;top:82px;width:148px"><span>2016</span><span>2018</span><span>2020</span><span>2022</span><span>2024</span></div>
</section>

<section class="slide dark">
  <h3 class="hd">Dashboard</h3>
  <div class="box" style="left:9px;top:20px;width:82px;height:58px"></div>
  <div class="abs" style="left:9px;top:78px;width:82px;height:4px;background:var(--line-dark);border-radius:0 0 3px 3px"></div>
  <svg class="abs" style="left:14px;top:30px" width="72" height="42" viewBox="0 0 72 42"><polyline points="0,36 12,27 24,30 36,17 48,21 60,9 72,4" fill="none" stroke="#f0892a" stroke-width="2"/></svg>
  <p class="num" style="left:98px;top:22px">1,240</p><p class="p" style="left:98px;top:32px">Active users</p>
  <p class="num" style="left:98px;top:44px">86%</p><p class="p" style="left:98px;top:54px">Uptime score</p>
  <p class="p" style="left:98px;top:66px;width:64px">Live view of your key numbers.</p>
</section>
<section class="slide dark">
  <h3 class="hd">Introduction</h3>
  <p class="p" style="left:9px;top:20px;width:72px">Nexora helps small and medium businesses adopt the right digital tools. We plan, build and support systems that save time.</p>
  <p class="p" style="left:90px;top:20px;width:72px">Our team blends strategy, design and engineering so every client gets clear advice and lasting results.</p>
  <div class="btn" style="left:9px;top:76px">Read More</div>
</section>
<section class="slide dark">
  <h3 class="hd">Global Reach</h3><p class="sub">Clients in 18 countries</p>
  <div class="mapfill" style="left:12px;top:24px;width:110px;height:62px" role="img" aria-label="World map"></div>
  <svg class="ic fo" style="left:38px;top:36px" width="7" height="7"><use href="#i-pin"/></svg><svg class="ic fo" style="left:74px;top:33px" width="7" height="7"><use href="#i-pin"/></svg><svg class="ic fo" style="left:100px;top:58px" width="7" height="7"><use href="#i-pin"/></svg>
  <p class="num" style="left:128px;top:28px">18</p><p class="p" style="left:128px;top:38px">Countries</p>
  <p class="num" style="left:128px;top:52px">3</p><p class="p" style="left:128px;top:62px">Regions</p>
</section>
<section class="slide dark">
  <h3 class="hd">Locations</h3>
  <div class="mapfill" style="left:10px;top:20px;width:100px;height:66px" role="img" aria-label="United States map"></div>
  <svg class="ic fo" style="left:30px;top:38px" width="7" height="7"><use href="#i-pin"/></svg><svg class="ic fo" style="left:86px;top:46px" width="7" height="7"><use href="#i-pin"/></svg>
  <p class="h5" style="left:116px;top:26px">West Office</p><p class="p" style="left:116px;top:33px">Sales and support</p>
  <p class="h5" style="left:116px;top:46px">East Office</p><p class="p" style="left:116px;top:53px">Engineering</p>
</section>
<section class="slide dark">
  <div class="ph" style="left:0;top:0;width:171px;height:96px;background:linear-gradient(135deg,#5c6670,#2f3944)" role="img" aria-label="Office background in grey"></div>
  <h2 class="big" style="left:12px;top:30px">Thank You</h2>
  <svg class="ic" style="left:12px;top:50px" width="5" height="5"><use href="#i-phone"/></svg><p class="p w" style="left:19px;top:50px">+1 000 555 0199</p>
  <svg class="ic" style="left:12px;top:59px" width="5" height="5"><use href="#i-mail"/></svg><p class="p w" style="left:19px;top:59px">hello@nexora.co</p>
</section>

</main>
</body>
</html>
```